Restyle Company web site and logo

we need a wordpress design beacause after few year we need to refresh our company web site(www.velantoworks.net) & logo. We are a small company called KR Advisory focused on business intellegence, data quality, data integration, etc and based on Legnago (small town near to Verona (italy)).
During the 2014 we add to our skill develop project for MDM and Procurement.
We are Young (avg 30 years old). We want to change our logo and color templete to communicate to all cumstomer professional skill, precision and passion.

--- UPDATE --
The new site can be complitile different from the actual website.
The new Logo is now available.

Target Market(s)

B2B, mid size market, professional account

Industry/Entity Type

It Company

Font styles to use
Sans Serif

Colors
acd037
3277b5

Requirements
Must have
• Simple and clean/clear image colur. Professional site. it need to rapresent trust site.
• Must be responsive desk/mobile.
Nice to have
• different color area for different kind off business line.
• slider image.
Should not have
• classical image

```html
<!DOCTYPE html>
<html lang="en">
<head>
<meta charset="utf-8">
<title>KR Advisory</title>
<link href="https://fonts.googleapis.com/css2?family=Open+Sans+Condensed:wght@300;700&family=Arimo:wght@400;700&display=swap" rel="stylesheet">
<style>
:root{
  --sky:#47acc8;
  --navy:#0a5e95;
  --lime:#9cc800;
  --olive:#6e9112;
  --coral:#de8367;
  --teal:#47acc8;
  --royal:#3f6dc4;
  --card:#f2f0f4;
  --cardhead:#e8e5e8;
  --ink:#1a1a1a;
  --footer:#333335;
  --footer-bottom:#2a2a2b;
  --footer-text:#b4b4b4;
}
*{box-sizing:border-box;margin:0;padding:0}
html,body{width:993px;height:1200px;overflow:hidden;background:#fff;font-family:"Arimo",Arial,sans-serif;color:var(--ink)}
.page{position:relative;width:993px;height:1200px}
.cond{font-family:"Open Sans Condensed","Arial Narrow",sans-serif}

.site-header{position:absolute;left:0;top:0;width:993px;height:122px;background:var(--sky)}
.brand{position:absolute;left:48px;top:0;width:170px;height:122px;background:#fff;display:flex;flex-direction:column;align-items:center;justify-content:center;gap:8px}
.brand-dot{width:26px;height:26px;border-radius:50%;background:var(--lime)}
.brand-name{font-size:16px;color:var(--navy);letter-spacing:.5px}
.nav-active{position:absolute;left:218px;top:0;width:77px;height:122px;background:var(--navy)}
.main-nav{position:absolute;top:62px;left:0;height:40px}
.nav-item{position:absolute;display:flex;flex-direction:column;align-items:center;color:#fff;font-family:"Open Sans Condensed",sans-serif;font-weight:700;font-size:11.5px;white-space:nowrap;transform:translateX(-50%)}
.nav-item svg{width:15px;height:15px;margin-bottom:6px;fill:#fff}

.hero{position:absolute;left:0;top:122px;width:993px;height:334px;background:linear-gradient(120deg,#b9c4c6 0%,#e4e8ea 35%,#f2f3f3 60%,#dfe3e4 100%)}
.hero-dots{position:absolute;right:45px;top:22px;display:flex;gap:8px}
.hero-dots span{width:10px;height:10px;border-radius:50%;background:var(--navy)}
.hero-dots span:first-child{background:var(--lime)}
.hero-copy{position:absolute;left:496px;top:125px;width:448px}
.hero-title{font-weight:300;font-size:52px;line-height:58px;color:#111;border-bottom:2px solid var(--lime);padding-bottom:0}
.hero-text{font-size:11.5px;line-height:15px;margin-top:11px;width:395px}

.card{position:absolute;top:492px;width:273px;height:287px;background:var(--card)}
.card-head{height:53px;background:var(--cardhead);display:flex;align-items:center}
.card-icon{width:53px;height:53px;display:flex;align-items:center;justify-content:center}
.card-icon svg{width:22px;height:22px;fill:#fff}
.card-title{font-weight:300;font-size:29px;margin-left:12px;color:#222}
.card-body{padding:21px 22px 0 23px;font-size:10.5px;line-height:15px;color:#222}
.btn{display:inline-block;color:#fff;font-size:10.5px;padding:4px 9px;margin-top:8px}
.mission .card-icon,.mission .btn{background:var(--coral)}
.partners .card-icon,.partners .btn{background:var(--teal)}
.work .card-icon,.work .btn{background:var(--royal)}

.callout{position:absolute;left:48px;top:799px;width:898px;height:157px;background:var(--lime)}
.callout-side{position:absolute;left:0;top:0;width:97px;height:157px;background:var(--olive);display:flex;align-items:center;justify-content:center}
.callout-title{position:absolute;left:121px;top:20px;font-weight:700;font-size:24px;line-height:26px;color:#fff}
.callout-text{position:absolute;left:121px;top:82px;width:770px;font-size:10.5px;line-height:15px;color:#fff}
.callout-btn{position:absolute;right:0;bottom:0;background:#4a6410;color:#fff;font-size:10.5px;padding:5px 10px}

.site-footer{position:absolute;left:0;top:981px;width:993px;height:176px;background:var(--footer)}
.footer-bar{position:absolute;top:0;left:386px;height:3px;width:395px;background:linear-gradient(90deg,#3a7fa8 50%,var(--lime) 50%)}
.footer-brand{position:absolute;left:48px;top:30px;font-size:17px;color:var(--navy)}
.footer-address{position:absolute;left:48px;top:114px;font-size:9.5px;line-height:15px;color:#ddd}
.footer-head{font-weight:700;font-size:12.5px;color:#fff;margin-bottom:10px}
.footer-nav{position:absolute;left:388px;top:35px}
.footer-nav li{list-style:none;font-size:9.5px;color:var(--footer-text);line-height:18px}
.newsletter{position:absolute;left:564px;top:35px}
.subscribe{display:flex}
.subscribe span{width:122px;height:26px;background:#4a4a4c;color:#999;font-size:10px;padding:7px 8px}
.subscribe b{height:26px;background:var(--navy);color:#fff;font-family:"Open Sans Condensed",sans-serif;font-size:10.5px;padding:7px 10px}
.community{margin-top:16px}
.socials{display:flex;gap:5px}
.socials span{width:20px;height:20px}
.footer-bottom{position:absolute;left:0;top:1157px;width:993px;height:43px;background:var(--footer-bottom);font-size:10.5px;color:#999}
.footer-bottom .copy{position:absolute;left:48px;top:16px}
.footer-bottom .policy{position:absolute;right:48px;top:16px}
</style>
</head>
<body>
<div class="page">
  <header class="site-header">
    <div class="brand"><span class="brand-dot"></span><span class="brand-name">KR Advisory</span></div>
    <div class="nav-active"></div>
    <nav class="main-nav">
      <div class="nav-item" style="left:262px;top:2px"><svg viewBox="0 0 16 16" style="position:relative;top:-2px"><path d="M8 1 0 8h2v7h4v-4h4v4h4V8h2z"/></svg>HOME ⌄</div>
      <div class="nav-item" style="left:358px"><svg viewBox="0 0 16 16"><circle cx="5" cy="4" r="3"/><circle cx="11" cy="4" r="3"/><path d="M0 15c0-5 2-7 5-7s5 2 5 7zM8 15c0-4 1-7 3-7 3 0 5 2 5 7z"/></svg>BUSINESS PARTNER ⌄</div>
      <div class="nav-item" style="left:466px"><svg viewBox="0 0 16 16"><path d="M15 1C9 1 5 5 4 9l3 3c4-1 8-5 8-11zM3 10l-2 5 5-2z"/></svg>OUR MISSION</div>
      <div class="nav-item" style="left:565px"><svg viewBox="0 0 16 16"><path d="M4 1h9v12H5l-1 2V1z"/></svg>REFERENCE ⌄</div>
      <div class="nav-item" style="left:659px"><svg viewBox="0 0 16 16"><path d="M5 2h6v2h4v11H1V4h4zm1 1v1h4V3z"/></svg>WORK WITH US</div>
      <div class="nav-item" style="left:760px"><svg viewBox="0 0 16 16"><path d="M1 9c3-4 11-4 14 0l-2 2-3-1V8H6v2l-3 1z"/></svg>CONTACT US</div>
      <div class="nav-item" style="left:843px"><svg viewBox="0 0 16 16"><path d="M7 1a6 6 0 1 0 3.5 10.9L14 15l1.4-1.4-3.3-3.4A6 6 0 0 0 7 1zm0 2a4 4 0 1 1 0 8 4 4 0 0 1 0-8z"/></svg>SEARCH</div>
    </nav>
  </header>

  <section class="hero" role="img" aria-label="Slider photo: a ballpoint pen resting on printed financial reports with a pie chart">
    <div class="hero-dots"><span></span><span></span><span></span><span></span><span></span></div>
    <div class="hero-copy">
      <h1 class="hero-title cond">Business Intelligence</h1>
      <p class="hero-text">The information that drives your business. How many people in your company have the right information at the right time and in the correct form? KR Advisory helps you get all the information you need in the most...</p>
    </div>
  </section>

  <article class="card mission" style="left:47px">
    <div class="card-head"><div class="card-icon"><svg viewBox="0 0 16 16"><path d="M15 1C9 1 5 5 4 9l3 3c4-1 8-5 8-11zM3 10l-2 5 5-2z"/></svg></div><h2 class="card-title cond">Our Mission</h2></div>
    <div class="card-body">For a company it is essential to exploit the wealth of information available to make them accessible to their managers in order to help them in choosing the right business strategies (see the trend of performance, generate estimates, assume future scenarios and future strategies of response.) KR Advisory helps you to manage this process as simple and fast!<br><span class="btn">Read More</span></div>
  </article>
  <article class="card partners" style="left:360px">
    <div class="card-head"><div class="card-icon"><svg viewBox="0 0 16 16"><circle cx="5" cy="4" r="3"/><circle cx="11" cy="4" r="3"/><path d="M0 15c0-5 2-7 5-7s5 2 5 7zM8 15c0-4 1-7 3-7 3 0 5 2 5 7z"/></svg></div><h2 class="card-title cond">Business Partners</h2></div>
    <div class="card-body">For a company it is essential to exploit the wealth of information available to make them accessible to their managers in order to help them in choosing the right business strategies (see the trend of performance, generate estimates, assume future scenarios and future strategies of response.) KR Advisory helps you to manage this process as simple and fast!<br><span class="btn">Read More</span></div>
  </article>
  <article class="card work" style="left:672px">
    <div class="card-head"><div class="card-icon"><svg viewBox="0 0 16 16"><path d="M5 2h6v2h4v11H1V4h4zm1 1v1h4V3z"/></svg></div><h2 class="card-title cond">Work with Us</h2></div>
    <div class="card-body">For a company it is essential to exploit the wealth of information available to make them accessible to their managers in order to help them in choosing the right business strategies (see the trend of performance, generate estimates, assume future scenarios and future strategies of response.) KR Advisory helps you to manage this process as simple and fast!<br><span class="btn">Read More</span></div>
  </article>

  <section class="callout">
    <div class="callout-side"><svg width="42" height="42" viewBox="0 0 42 42"><circle cx="21" cy="21" r="21" fill="#fff"/><path d="M18 10v12l6 7" stroke="#6e9112" stroke-width="5" fill="none"/></svg></div>
    <h2 class="callout-title cond">How many people in your company have the desired information<br>at the right time and in the correct form?</h2>
    <p class="callout-text">For a company it is essential to exploit the wealth of information available to make them accessible to their managers in order to help them in choosing the right business strategies (see the trend of performance, generate estimates, assume future scenarios and future strategies of response.) KR Advisory helps you to manage this process as simple and fast!</p>
    <span class="callout-btn">Read More</span>
  </section>

  <footer class="site-footer">
    <div class="footer-bar"></div>
    <div class="footer-brand">KR Advisory</div>
    <p class="footer-address">Via Lorenzo Ferri, 24/B<br>37100 Castelmonte (VR)<br>Italy</p>
    <div class="footer-nav cond">
      <h3 class="footer-head">Navigations</h3>
      <ul><li>Home</li><li>Business Partner</li><li>Reference</li><li>Work With Us</li><li>Contact Us</li></ul>
    </div>
    <div class="newsletter">
      <h3 class="footer-head cond">Subscribe Email Newsletter</h3>
      <div class="subscribe"><span>Your Email</span><b>SUBSCRIBE</b></div>
      <h3 class="footer-head cond community">Join Our Community</h3>
      <div class="socials"><span style="background:#1fa3c9"></span><span style="background:#2f5aa8"></span><span style="background:#1070b8"></span><span style="background:#c4302b"></span></div>
    </div>
  </footer>
  <div class="footer-bottom"><span class="copy">© Copyright KR Advisory S.r.l. 2014. All Rights Reserved.</span><span class="policy">Privacy Policy</span></div>
</div>
</body>
</html>
```